Business Card Design Project

We need a business card design for a new construction company called 'KORVA HOLDINGS PTY.LTD' We run a construction based company for high end market homes in melbourne, we want something that looks professional and eye catching.The card needs to have a strong design to it something modern as the company name explains "korva." The final design should communicate professionalism and a strong image to our customers on the quality of our work.
On the business card i need
Name: Marek Holtvay
Mob:0417295031
Email:korva.holdings@mailbrook.example
Domestic/Residential/Commercial

```html
<!DOCTYPE html>
<html lang="en">
<head>
<meta charset="utf-8">
<title>Korva Holdings – Business Card</title>
<link rel="stylesheet" href="https://fonts.googleapis.com/css2?family=Arimo:wght@400;700&display=swap">
<style>
  :root {
    --backdrop: #e6e6e6;
    --cream: #ffffd2;
    --red-main: #cc0000;
    --red-bright: #ff0000;
    --red-accent: #e3202a;
    --ink: #1f1f1f;
    --card-text: #fff6cf;
  }
  * { box-sizing: border-box; margin: 0; padding: 0; }
  html, body {
    width: 1200px;
    height: 1200px;
    overflow: hidden;
    background: var(--backdrop);
    font-family: "Arimo", Arial, sans-serif;
  }
  .card {
    position: absolute;
    left: 128px;
    top: 302px;
    width: 944px;
    height: 538px;
    background: var(--red-main);
    overflow: hidden;
  }
  .brand-panel {
    position: absolute;
    left: 0;
    top: 0;
    width: 312px;
    height: 100%;
    background: var(--cream);
    display: flex;
    flex-direction: column;
    align-items: center;
    justify-content: center;
    gap: 14px;
  }
  .brand-stripe {
    position: absolute;
    left: 312px;
    top: 0;
    width: 14px;
    height: 100%;
    background: var(--red-bright);
  }
  .brand-name {
    font-size: 76px;
    font-weight: 700;
    line-height: 1;
    color: var(--ink);
  }
  .brand-tagline {
    font-size: 15px;
    font-weight: 400;
    letter-spacing: 0.3em;
    color: var(--red-accent);
    white-space: nowrap;
  }
  .contact {
    position: absolute;
    left: 364px;
    top: 140px;
    right: 24px;
    color: var(--card-text);
    white-space: nowrap;
  }
  .contact-name {
    font-size: 62px;
    font-weight: 700;
    line-height: 1;
    letter-spacing: 0.5px;
    margin-bottom: 26px;
  }
  .contact-line {
    font-size: 36px;
    font-weight: 400;
    line-height: 1;
    margin-bottom: 30px;
  }
  .contact-email {
    font-size: 32px;
    letter-spacing: -0.3px;
  }
  .contact-services {
    font-size: 34px;
    letter-spacing: -0.3px;
  }
</style>
</head>
<body>
  <div class="card">
    <div class="brand-panel">
      <span class="brand-name">korva</span>
      <span class="brand-tagline">HOLDINGS PTY.LTD</span>
    </div>
    <div class="brand-stripe"></div>
    <div class="contact">
      <p class="contact-name">Marek Holtvay</p>
      <p class="contact-line">0417295031</p>
      <p class="contact-line contact-email">korva.holdings@mailbrook.example</p>
      <p class="contact-line contact-services">Domestic/Residential/Commercial</p>
    </div>
  </div>
</body>
</html>
```